National Sales Conference

We need a cool one page flyer inviting our sales partners to a National Sales Training Class.

Most important event in 5 years! Do not even consider missing it

Details of Sales Meeting
Nov 10th - 11th in Dallas, TX
Nov 10th (welcome party) 7-9pm

Preliminary Agenda
Nov, 10th 7-9pm Welcome Reception

Nov 11th and 12th 9-4 Tillpoint Drill Week Sales training. Learn the tools you need to become more relevant in the marketplace as we launch multiple new cutting edge products and services. Many vendors will be on hand to personally meet you and provide the tools and marketing information you need.

Location of event
Kelbrook Plaza Lodge West
2876 Harlowmere Pkwy.
Fort Worth, TX 76392
FREE Shuttle from DFW!
Updates

Please put the Brightwater Vendor Solutions logo at the TOP left and the Quillstone Remit logo make it small and near the bottom

Add the following TEXT. 

*** This event is so important our CEO, Marcus Delong has decided that we are covering all of the expenses! That's right, we will provide the sleeping room based on double occupancy, all meals, and with 10 deals in 90 days we will even reimburse your airfare if a flight is necessary. 

Be sure to include the RSVP information and lines for the to print out and check if they are coming or not as indicated in the original brief. 

This flyer will be sent to our sales agents VIA Email in PDF. Therefore, if we need to make it 2 pages so it is not so cluttered, I'm okay with that. 

Target Market(s)

Our Sales Agents

Industry/Entity Type

Training

Requirements
Must have
• One page! High energy will a strong call to action.
• Needs a small fill in the blank for an RSVP
• Name _______________
• Check Box YES! I will gladly attend. _____ # attending
• Check Box Can't make it.
• Fax RSVP to 775-319-2740 or email marcusd@brightwaterco.example

```html
<!DOCTYPE html>
<html lang="en">
<head>
<meta charset="utf-8">
<title>National Sales Conference</title>
<link rel="stylesheet" href="https://fonts.googleapis.com/css2?family=Oswald:wght@600;700&family=Cinzel:wght@400&family=Didact+Gothic&display=swap">
<style>
  :root {
    --blue: #1f6fc8;
    --blue-deep: #1358b0;
    --box-blue: #2d6fd0;
    --green: #8cc63f;
    --text-blue: #6e9edb;
    --ink: #1a1a1a;
    --white: #ffffff;
    --paper: #ffffff;
  }
  * { margin: 0; padding: 0; box-sizing: border-box; }
  html, body { width: 1200px; height: 2740px; overflow: hidden; background: var(--paper); }
  body { font-family: "Didact Gothic", "Century Gothic", sans-serif; color: var(--ink); }
  .flyer { position: relative; width: 1200px; height: 2740px; overflow: hidden; background: var(--paper); }

  .hero-photo {
    position: absolute; left: 0; top: 0; width: 1200px; height: 1137px;
    background: linear-gradient(160deg, #f4f6f8 0%, #dfe4ea 35%, #c9ced6 60%, #eef0f2 100%);
  }
  .brand {
    position: absolute; top: 62px; right: 60px;
    display: flex; align-items: center; gap: 18px;
    font-size: 40px; color: var(--blue-deep);
  }
  .brand-mark { width: 46px; height: 46px; background: var(--blue-deep); }

  .headline { position: absolute; left: 28px; top: 680px; line-height: 0.92; }
  .headline-big {
    display: block; font-family: "Oswald", sans-serif; font-weight: 700;
    font-size: 168px; color: var(--blue); text-transform: uppercase; letter-spacing: -2px;
  }
  .headline-small {
    display: block; font-family: "Oswald", sans-serif; font-weight: 700;
    font-size: 120px; color: var(--ink); text-transform: uppercase; margin-top: 14px;
    -webkit-text-stroke: 4px var(--white); paint-order: stroke fill;
  }

  .tagline {
    position: absolute; top: 1175px; left: 0; width: 1200px; text-align: center;
    font-family: "Cinzel", serif; font-size: 52px; color: var(--blue); letter-spacing: 1px;
  }

  .details-band {
    position: absolute; top: 1247px; left: 0; width: 1200px; height: 220px; background: var(--green);
  }
  .rsvp-form { position: absolute; left: 50px; top: 22px; width: 540px; font-size: 21px; line-height: 1.4; color: var(--ink); }
  .rsvp-form .contact { margin-top: 6px; }
  .fill-line { display: inline-block; border-bottom: 2px solid var(--ink); height: 20px; vertical-align: baseline; }
  .fill-line.name { width: 300px; }
  .fill-line.count { width: 54px; }
  .check-box { display: inline-block; width: 18px; height: 18px; border: 2px solid var(--ink); background: var(--white); margin-right: 8px; vertical-align: -2px; }
  .meeting-details { position: absolute; right: 50px; top: 30px; text-align: right; font-size: 38px; line-height: 1.22; color: var(--ink); }
  sup { font-size: 0.55em; }

  .agenda-title {
    position: absolute; top: 1520px; left: 0; width: 1200px; text-align: center;
    font-family: "Cinzel", serif; font-size: 50px; color: var(--blue);
  }
  .agenda-box { position: absolute; top: 1625px; height: 162px; padding: 20px 24px; font-size: 36px; line-height: 1.15; }
  .agenda-box.reception { left: 156px; width: 425px; background: var(--box-blue); color: var(--ink); }
  .agenda-box.training { left: 597px; width: 452px; background: var(--green); color: var(--ink); }
  .caps { text-transform: uppercase; }

  .copy { position: absolute; left: 156px; width: 900px; font-size: 31px; line-height: 1.3; color: var(--text-blue); }
  .copy.intro { top: 1818px; }
  .copy.expenses { top: 2030px; }

  .venue-photo {
    position: absolute; left: 184px; top: 2247px; width: 424px; height: 288px;
    background: linear-gradient(180deg, #2a66c8 0%, #5b8fd8 45%, #8a6d5a 70%, #bcb7ae 100%);
  }
  .venue-box {
    position: absolute; left: 625px; top: 2247px; width: 370px; height: 288px;
    background: var(--box-blue); color: var(--white); padding: 52px 30px 0 30px;
    font-size: 24px; line-height: 1.35;
  }
  .venue-box .label { text-transform: uppercase; margin-bottom: 28px; font-size: 25px; }
  .venue-box .shuttle { margin-top: 22px; color: var(--ink); font-size: 25px; }

  .footer-contact { position: absolute; top: 2560px; left: 0; width: 1200px; text-align: center; font-size: 26px; color: var(--ink); }
  .partner {
    position: absolute; left: 862px; top: 2635px; display: flex; align-items: center; gap: 10px;
    font-size: 24px; color: var(--blue);
  }
  .partner-dot { width: 40px; height: 40px; border-radius: 50%; background: var(--green); }
</style>
</head>
<body>
<main class="flyer">
  <div class="hero-photo" role="img" aria-label="Photo of three smiling business colleagues seated at a meeting table in a bright office"></div>

  <div class="brand"><span class="brand-mark"></span><span>Brightwater Vendor Solutions</span></div>

  <h1 class="headline">
    <span class="headline-big">Most</span>
    <span class="headline-big">Important</span>
    <span class="headline-small">Event in 5 Years</span>
  </h1>

  <p class="tagline">DO NOT EVEN CONSIDER MISSING IT</p>

  <section class="details-band">
    <div class="rsvp-form">
      <p>Name <span class="fill-line name"></span></p>
      <p><span class="check-box"></span>YES! I will gladly attend. <span class="fill-line count"></span> # attending</p>
      <p><span class="check-box"></span>Can't make it.</p>
      <p class="contact">Fax RSVP to 775-319-2740<br>Email : marcusd@brightwaterco.example</p>
    </div>
    <p class="meeting-details">
      DETAILS OF SALES MEETING<br>
      Nov 10<sup>th</sup> - 11<sup>th</sup> in Dallas, TX<br>
      Nov 10<sup>th</sup> (welcome party) 7-9pm
    </p>
  </section>

  <h2 class="agenda-title">PRELIMINARY AGENDA</h2>

  <div class="agenda-box reception">Nov, 10<sup>th</sup> 7-9pm<br><span class="caps">Welcome Reception</span></div>
  <div class="agenda-box training">Nov 11<sup>th</sup> and 12<sup>th</sup> 9-4<br><span class="caps">Tillpoint Drill Week<br>Sales Training</span></div>

  <p class="copy intro">Learn the tools you need to become more relevant in the marketplace as we launch multiple new cutting edge products and services. Many vendors will be on hand to personally meet you and provide the tools and marketing information you need.</p>

  <p class="copy expenses">*** This event is so important our CEO, Marcus Delong has decided that we are covering all of the expenses! That's right, we will provide the sleeping room based on double occupancy, all meals, and with 10 deals in 90 days we will even reimburse your airfare if a flight is necessary</p>

  <div class="venue-photo" role="img" aria-label="Photo of the hotel exterior at dusk with the entrance canopy and tower"></div>
  <div class="venue-box">
    <p class="label">Location of Event</p>
    <p>Kelbrook Plaza Lodge West<br>2876 Harlowmere Pkwy.<br>Fort Worth, TX 76392</p>
    <p class="shuttle">FREE Shuttle from DFW!</p>
  </div>

  <p class="footer-contact">Fax RSVP to 775-319-2740 &nbsp; Email : marcusd@brightwaterco.example</p>

  <div class="partner"><span class="partner-dot"></span><span>Quillstone Remit</span></div>
</main>
</body>
</html>
```